Real Estate "For Sale" Sign for construction company

We need a sign that we can use to hang on a post and place on the road when we sell a property. The sign will be simple and will need to mainly feature our logo (files attached), as well as the words "For Sale", and then our phone number "(555) 617 3489". The sign will hang on a post that'll look something like the attached picture.

Target Market(s)

Home buyers

Industry/Entity Type

Real Estate

Font styles to use
Serif
Sans Serif

Colors
0054AA
0677BA
7BADD7
CADEEF
E8F1F8
0094D4
00A9DD
6FCCEA
C7EBF8
E9F6FB

Requirements
Must have
• For Sale & our phone number

```html
<!DOCTYPE html>
<html lang="en">
<head>
<meta charset="utf-8">
<title>For Sale Sign – Bluecrest Ridge Homes</title>
<link rel="stylesheet" href="https://fonts.googleapis.com/css2?family=Bebas+Neue&family=Montserrat:wght@500;700&display=swap">
<style>
  :root {
    --page-bg: #f7f7f7;
    --sign-bg: #8fd8f7;
    --navy: #14214f;
    --brand-blue: #1b7fc4;
  }
  * { margin: 0; padding: 0; box-sizing: border-box; }
  html, body {
    width: 1200px;
    height: 814px;
    overflow: hidden;
    background: var(--page-bg);
  }
  .canvas {
    width: 1200px;
    height: 814px;
    display: flex;
    align-items: center;
    justify-content: center;
  }
  .sign {
    position: relative;
    width: 538px;
    height: 760px;
    background: var(--sign-bg);
    text-align: center;
  }
  .brand {
    position: absolute;
    top: 44px;
    left: 0;
    right: 0;
    display: flex;
    flex-direction: column;
    align-items: center;
  }
  .brand-mark {
    width: 120px;
    height: 120px;
    border-radius: 50%;
    background: var(--brand-blue);
    margin-bottom: 18px;
  }
  .brand-name {
    font-family: "Montserrat", sans-serif;
    font-weight: 500;
    font-size: 33px;
    letter-spacing: 0.5px;
    color: var(--brand-blue);
    line-height: 1;
  }
  .headline {
    position: absolute;
    top: 268px;
    left: 0;
    right: 0;
    font-family: "Montserrat", sans-serif;
    font-weight: 700;
    font-size: 196px;
    line-height: 162px;
    letter-spacing: -4px;
    color: var(--navy);
  }
  .headline span { display: block; }
  .phone {
    position: absolute;
    top: 656px;
    left: 0;
    right: 0;
    font-family: "Bebas Neue", sans-serif;
    font-size: 90px;
    line-height: 1;
    letter-spacing: 0;
    color: var(--navy);
  }
</style>
</head>
<body>
  <main class="canvas">
    <section class="sign">
      <div class="brand">
        <div class="brand-mark"></div>
        <p class="brand-name">Bluecrest Ridge Homes</p>
      </div>
      <h1 class="headline"><span>FOR</span><span>SALE</span></h1>
      <p class="phone">(555) 617 3489</p>
    </section>
  </main>
</body>
</html>
```